WordPress website in children books redesign

We are personalised children storybook creators with a range of personalized books, music CDs and DVDs that are created for each child. We sell our concept through a license via distributors / entrepreneurs mainly based in France and Europe. We want to focus on selling B2C to parents and grandparents, looking to buy presents to their children aged 0 to 10 years old. Those present are educative, unique for each child, and they will learn to have fun and learn to have fun. I would like to redesign our WordPress website https://pebblelanternkids.co.uk/index.php We are a children in the world of books and music books: books, music CDs and DVDs looking for something a little more along the lines of our competitors. See ike www.quillotop.com, www.tavirosa.com, www.lecheminduvelours.com, https://www.lespetitsbrume.com/, https://tinselpaths.com/ Our current website is a bit too old fashioned so I am looking at a much more modern design Here is a link for a few products that are not available here: https://www.filecrate.example/sh/kq417dzopfrnwtb/BXPL3rYmOk2u-sVH4dQkLN-zb?dl=0 We have 2 sides in our website: B2C on the left side and B2B on the right site; B2B is for distributors that are entrepreneurs buying our concept. for the homepage design, the main focus will be B2Consumer Our current page is too blended, lacks reassurance elements and I would like to have a look at this page. from our current stories. here is a link for our business book to give you a feel for it: http://online.pagewavo.com/qtlk/pzme/ MAIN PAGES TO REVIEW / HOMEPAGE / https://pebblelanternkids.co.uk/ BOOKS: https : //pebblelanternkids.co.uk/product-category/personalised-books/ MUSIC: https://pebblelanternkids.co.uk/product-category/music-cds/ BLOG: https://pebblelanternkids.co.uk/blog -2 / Looking forward to seeing you and your questions asap

Target Market(s)

parents and grandparents of children aged 0 to 10 years old. This is for the European market

Industry/Entity Type

Publishing Company

Number of Pages Required

4 page

Colors
0392cd
9bcb3b
ec1f27
757575

Requirements
Must have
• keep within the color code of our RGB logo: D25028 RGB: 8CC364 329BC8 808285
Nice to have
• be more with the style of our competitors. Pebble Lantern Kids am about making children learn the fun way, and develop their morality, self-esteem and confidence. It's about the magic of reading to help children learn while having fun. I have attached visuals but those are just examples and you we encourage you to suggest other ideas

```html
<!DOCTYPE html>
<html lang="en">
<head>
<meta charset="utf-8">
<title>Pebble Lantern Kids – Personalised Children's Books</title>
<link href="https://fonts.googleapis.com/css2?family=Baloo+2:wght@600;800&family=Open+Sans:wght@400;600;700&display=swap" rel="stylesheet">
<style>
:root{
  --blue:#0392cd;
  --blue-deep:#075c88;
  --green:#9bcb3b;
  --green-dark:#6fa826;
  --red:#ec1f27;
  --orange:#d25028;
  --grey:#757575;
  --ink:#2b2b2b;
  --sky:#e3f2fb;
  --purple:#5b3a8c;
  --yellow:#f4c21c;
  --white:#ffffff;
}
*{box-sizing:border-box;margin:0;padding:0}
html,body{width:1200px;height:4732px;overflow:hidden}
body{position:relative;font-family:"Open Sans",Arial,sans-serif;color:var(--grey);background:var(--white)}
.abs{position:absolute}
.display{font-family:"Baloo 2","Trebuchet MS",sans-serif;font-weight:800}
.ph{position:absolute}

/* header */
.site-header{position:absolute;left:0;top:0;width:1200px;height:120px;background:var(--white)}
.brand{position:absolute;left:40px;top:28px;display:flex;align-items:center;gap:10px}
.brand-dot{width:44px;height:44px;border-radius:50%;background:var(--green)}
.brand-name{font-family:"Baloo 2",sans-serif;font-weight:800;font-size:24px;color:var(--blue)}
.cart-btn{position:absolute;right:90px;top:12px;background:var(--orange);color:#fff;font-size:11px;font-weight:700;padding:7px 14px;border-radius:2px;letter-spacing:.5px}
.main-nav{position:absolute;right:90px;top:84px;display:flex;gap:34px;font-size:12px;font-weight:700;color:var(--ink);letter-spacing:.6px}

/* hero */
.hero{position:absolute;left:0;top:120px;width:1200px;height:672px;background:linear-gradient(#b8dc5a,var(--green) 60%,var(--green-dark))}
.hero-title{position:absolute;left:430px;top:232px;width:430px;color:#fff;font-size:36px;line-height:40px;text-align:center}
.hero-btn{position:absolute;left:444px;top:352px;background:#fff;color:var(--ink);font-size:14px;font-weight:700;padding:9px 20px;border-radius:20px}

/* video */
.video-block{position:absolute;left:320px;top:860px;width:320px;height:210px;background:linear-gradient(135deg,#d9d3cb,#8f8a86)}
.play{position:absolute;left:130px;top:80px;width:60px;height:42px;border-radius:10px;background:rgba(0,0,0,.75)}
.play:after{content:"";position:absolute;left:24px;top:12px;border-left:16px solid #fff;border-top:9px solid transparent;border-bottom:9px solid transparent}
.intro{position:absolute;left:672px;top:850px;width:470px}
.intro h2{color:var(--blue);font-size:30px;line-height:34px}
.intro p{margin-top:16px;font-size:13px;line-height:20px}
.more-link{display:inline-block;margin-top:12px;color:var(--blue);font-weight:700;font-size:13px;border-bottom:2px solid var(--blue)}

/* heroes */
.heroes-title{position:absolute;left:660px;top:1590px;width:480px;text-align:center;color:var(--red);font-size:34px;line-height:36px}
.outline-btn{position:absolute;border:2px solid var(--ink);color:var(--ink);font-weight:700;font-size:14px;padding:8px 18px;background:#fff}

/* vision / mission */
.purpose{position:absolute;left:0;top:1860px;width:1200px;height:470px;background:var(--blue)}
.purpose-col{position:absolute;top:80px;width:400px;color:#fff}
.purpose-col h3{font-size:36px;line-height:40px}
.purpose-col h3:after{content:"";display:block;width:40px;height:3px;background:#fff;margin-top:6px}
.purpose-col p{margin-top:22px;font-size:13px;line-height:21px;color:#e5f4fb}

/* products */
.products{position:absolute;left:0;top:2330px;width:1200px;height:790px;background:var(--sky)}
.products-title{position:absolute;left:470px;top:125px;color:var(--ink);font-size:34px;line-height:36px}
.sign{position:absolute;width:130px;height:170px;border-radius:4px;color:#fff;text-align:center;font-weight:700;font-size:15px;line-height:18px;padding-top:104px}
.sign svg{position:absolute;left:37px;top:30px}
.num{position:absolute;width:38px;height:38px;border-radius:50%;color:#fff;font-weight:700;font-size:14px;line-height:38px;text-align:center}

/* distributor */
.dist-title{position:absolute;left:90px;top:3190px;color:var(--green-dark);font-size:36px}
.dist-sub{position:absolute;left:90px;top:3246px;color:var(--ink);font-weight:700;font-size:15px;letter-spacing:.6px}
.dist-copy{position:absolute;left:90px;top:3296px;width:450px;font-size:12.5px;line-height:19px}
.dist-copy p+p{margin-top:14px}
.dist-box{position:absolute;top:3340px;width:200px;height:130px;color:#fff;font-family:"Baloo 2",sans-serif;font-weight:800;font-size:22px;line-height:24px;text-align:center;display:flex;align-items:center;justify-content:center}

/* testimonial */
.ribbon{position:absolute;left:380px;top:3620px;width:440px;height:42px;background:var(--green);color:#fff;font-weight:700;font-size:16px;line-height:42px;text-align:center}
.quote-title{position:absolute;left:0;top:3690px;width:1200px;text-align:center;font-weight:700;color:var(--ink);font-size:16px}
.quote-text{position:absolute;left:270px;top:3728px;width:660px;text-align:center;font-size:13px;line-height:20px}
.arrow-btn{position:absolute;top:3735px;width:36px;height:36px;border-radius:50%;border:2px solid #bbb}

/* banner */
.banner{position:absolute;left:0;top:4020px;width:1200px;height:280px;background:linear-gradient(90deg,#d3ecf9,#eaf6fd)}
.banner h2{position:absolute;left:190px;top:40px;width:420px;color:var(--blue);font-size:34px;line-height:36px}
.banner p{position:absolute;left:190px;top:128px;width:400px;font-size:13px;line-height:20px}
.dark-btn{position:absolute;left:190px;top:190px;background:var(--ink);color:#fff;font-size:13px;font-weight:700;padding:9px 20px;border-radius:18px}

/* footer */
.site-footer{position:absolute;left:0;top:4320px;width:1200px;height:350px;background:var(--blue);color:#fff}
.foot-col{position:absolute;top:40px;font-size:12px;line-height:21px}
.foot-col h4{font-size:14px;margin-bottom:8px}
.foot-btn{display:inline-block;margin-top:10px;background:var(--green);color:#fff;font-weight:700;padding:5px 14px;font-size:12px}
.sub-field{display:inline-block;width:170px;height:34px;background:#fff;color:#999;font-size:12px;line-height:34px;padding-left:10px;vertical-align:middle}
.sub-btn{display:inline-block;height:34px;background:var(--yellow);color:var(--ink);font-weight:700;font-size:12px;line-height:34px;padding:0 18px;vertical-align:middle}
.social{display:inline-block;width:30px;height:30px;border-radius:50%;border:2px solid #fff;margin-right:8px;margin-top:16px}
.copyright{position:absolute;left:0;top:4670px;width:1200px;height:62px;background:var(--blue-deep);color:#d6ecf7;font-size:12px;line-height:62px;text-align:center}
</style>
</head>
<body>

<header class="site-header">
  <div class="brand"><span class="brand-dot"></span><span class="brand-name">Pebble Lantern Kids</span></div>
  <div class="cart-btn">CART · 0 ITEMS</div>
  <nav class="main-nav"><span>HOME</span><span>ABOUT US</span><span>OUR PRODUCTS</span><span>DISTRIBUTORS</span><span>BLOG</span><span>CONTACT US</span></nav>
</header>

<section class="hero" role="img" aria-label="Illustrated meadow scene with sun, flowers and grass">
  <div class="ph" role="img" aria-label="Illustration of children reading books on the grass" style="left:50px;top:290px;width:350px;height:330px;border-radius:8px;background:linear-gradient(#f2c27a,#c98a4e)"></div>
  <h1 class="hero-title display">Create the most personalised book for your child</h1>
  <div class="hero-btn">create your story</div>
  <div class="ph" role="img" aria-label="Stack of personalised storybooks" style="left:880px;top:220px;width:260px;height:330px;border-radius:6px;background:linear-gradient(135deg,#f0b44a,#2f7fc1)"></div>
</section>

<div class="video-block" role="img" aria-label="Video thumbnail of a child reading"><span class="play"></span></div>
<div class="intro">
  <h2 class="display">Personalisation Improves a Child's Learning Ability And Motivation</h2>
  <p>Our personalised books offer the possibility of sharing magical and unique moments which help the child become familiar with reading and inspire reading passion. What is more special and magical than becoming the hero of your own story!</p>
  <span class="more-link">Learn More</span>
</div>

<div class="ph" role="img" aria-label="Photo of a child in a sailor hat sitting on a suitcase holding a book" style="left:40px;top:1220px;width:590px;height:520px;background:linear-gradient(135deg,#e7ddd2,#9c6b4b)"></div>
<div class="ph" role="img" aria-label="Photo of a family reading together" style="left:668px;top:1220px;width:250px;height:130px;background:linear-gradient(135deg,#efe6dc,#b99a80)"></div>
<div class="ph" role="img" aria-label="Photo of a child with a book" style="left:930px;top:1220px;width:190px;height:130px;background:linear-gradient(135deg,#eef2f4,#9fb4c2)"></div>
<div class="ph" role="img" aria-label="Photo of children reading a personalised book" style="left:668px;top:1362px;width:452px;height:150px;background:linear-gradient(135deg,#d8c4a8,#4a6b8e)"></div>
<h2 class="heroes-title display">CHILDREN BECOME THE HEROES OF THEIR OWN STORIES</h2>
<div class="outline-btn" style="left:836px;top:1700px">Order Samples</div>

<section class="purpose">
  <div class="purpose-col" style="left:180px">
    <h3 class="display">Our Vision</h3>
    <p>It is to make children the heroes of fun adventures and live magical and unforgettable moments they can share with their family and friends.</p>
    <p>Scenarios are adapted to every age, imagined and conceived in association with children, schools, speech therapists, psychologists and childhood experts.</p>
  </div>
  <div class="purpose-col" style="left:612px">
    <h3 class="display">Our Mission</h3>
    <p>Personalisation offers the children to have an opportunity to recognise themselves in the story, thus developing the morals, self-esteem and confidence. All our stories aim to stimulate learning and enhance reading passion from an early age and have been designed with high quality original artwork with bright colours to fully engage a child's imagination. The stories are written in an educational and informative way, whilst remaining fun, positive and engaging.</p>
  </div>
  <div class="ph" role="img" aria-label="Small illustrated rocket" style="left:1020px;top:330px;width:50px;height:50px;border-radius:50%;background:linear-gradient(#f2f2f2,#e35d3c)"></div>
</section>

<section class="products">
  <div class="ph" role="img" aria-label="Illustrated white clouds" style="left:0;top:0;width:1200px;height:90px;background:linear-gradient(#ffffff,#e3f2fb)"></div>
  <div class="ph" role="img" aria-label="Illustrated wooden signpost" style="left:150px;top:90px;width:430px;height:620px;background:linear-gradient(#d9e6ee,#cddbe4)"></div>
  <h2 class="products-title display">Our product<br>collections</h2>
  <span class="num" style="left:90px;top:110px;background:var(--red)">01</span>
  <div class="sign" style="left:200px;top:170px;background:var(--red)"><svg width="56" height="56" viewBox="0 0 56 56"><path d="M6 12h18a4 4 0 0 1 4 4v30a4 4 0 0 0-4-4H6ZM50 12H32a4 4 0 0 0-4 4v30a4 4 0 0 1 4-4h18Z" fill="none" stroke="#fff" stroke-width="3"/></svg>Personalised<br>Books</div>
  <span class="num" style="left:600px;top:260px;background:var(--green)">02</span>
  <div class="sign" style="left:468px;top:270px;background:var(--green)"><svg width="56" height="56" viewBox="0 0 56 56"><circle cx="28" cy="28" r="22" fill="none" stroke="#fff" stroke-width="3"/><circle cx="28" cy="28" r="6" fill="#fff"/></svg>Music Cds</div>
  <span class="num" style="left:90px;top:460px;background:var(--purple)">03</span>
  <div class="sign" style="left:165px;top:470px;background:var(--purple)"><svg width="56" height="56" viewBox="0 0 56 56"><rect x="6" y="12" width="44" height="30" rx="3" fill="none" stroke="#fff" stroke-width="3"/><path d="M24 20l10 7-10 7Z" fill="#fff"/></svg>Cartoon Dvds</div>
  <span class="num" style="left:610px;top:500px;background:var(--yellow)">04</span>
  <div class="sign" style="left:470px;top:550px;background:var(--yellow);padding-top:96px"><svg width="56" height="56" viewBox="0 0 56 56"><path d="M28 6l6 14 15 1-11 10 4 15-14-8-14 8 4-15L7 21l15-1Z" fill="none" stroke="#fff" stroke-width="3"/></svg>Poems and<br>Books</div>
  <div class="ph" role="img" aria-label="Photo of two smiling children hugging" style="left:730px;top:110px;width:380px;height:600px;background:linear-gradient(#f0d2b4,#3f86c8)"></div>
  <div class="ph" role="img" aria-label="Illustrated grass strip" style="left:0;top:720px;width:1200px;height:70px;background:linear-gradient(#8cc364,#6fa826)"></div>
</section>

<h2 class="dist-title display">Become a Distributor</h2>
<div class="dist-sub">IT IS TIME TO LIVE YOUR DREAMS, RATHER THAN BUILDING SOMEONE ELSE'S!!</div>
<div class="dist-copy">
  <p>Our vision is to empower entrepreneurs to achieve professional success from the comfort of their home.</p>
  <p>At Pebble Lantern Kids, we believe it's time for you to harness your true potential. As a market leader and expert in distributing personalised children's books, we take great pride in offering a self-fulfilling career to those who wish to earn a substantial income from home.</p>
</div>
<div class="dist-box" style="left:585px;background:var(--blue)">Register<br>free webinars</div>
<div class="dist-box" style="left:800px;background:var(--orange)">Speak with<br>an advisor</div>

<div class="ribbon">What Distributors say about us</div>
<div class="quote-title">It's Fun to sell</div>
<p class="quote-text">This is my first year with the company and it is great to have a product that not only makes good profit but is also fun to sell. I am still amazed at the reaction I get from my customers the first time they see the products. I love it.</p>
<span class="arrow-btn" style="left:200px"><svg width="32" height="32" viewBox="0 0 32 32"><path d="M19 9l-7 7 7 7" fill="none" stroke="#777" stroke-width="2.5"/></svg></span>
<span class="arrow-btn" style="left:964px"><svg width="32" height="32" viewBox="0 0 32 32"><path d="M13 9l7 7-7 7" fill="none" stroke="#777" stroke-width="2.5"/></svg></span>
<div class="ph" role="img" aria-label="Portrait photo of the distributor" style="left:572px;top:3810px;width:56px;height:56px;border-radius:50%;background:linear-gradient(#c9a88c,#6b4a3a)"></div>

<section class="banner">
  <h2 class="display">Become the hero of your personalised story</h2>
  <p>Personalised books, nursery and school books, poems, activity books, games and much more</p>
  <span class="dark-btn">Learn More</span>
  <div class="ph" role="img" aria-label="Photo of a child lying down reading a book" style="left:640px;top:0;width:560px;height:280px;background:linear-gradient(90deg,#eaf6fd,#d9b99a)"></div>
</section>

<footer class="site-footer">
  <div class="foot-col" style="left:90px"><h4>Our Products</h4>Personalised books<br>Personalised music albums<br>Personalised DVD cartoon<br>Personalised school books<br><span class="foot-btn">Order samples</span></div>
  <div class="foot-col" style="left:300px"><h4>Distributors</h4>Becoming pack<br>Webinars<br>Material pack</div>
  <div class="foot-col" style="left:500px"><h4>Site Links</h4>Home<br>Success stories<br>About Us<br>Contact Us<br>Our concept<br>Blogs</div>
  <div class="foot-col" style="left:730px"><h4>Subscribe with us</h4><span class="sub-field">Enter your email</span><span class="sub-btn">Submit</span><br><span class="social"></span><span class="social"></span></div>
</footer>
<div class="copyright">© 2018 Pebble Lantern Kids. All Rights Reserved.</div>

</body>
</html>
```